Pivots & Treads .com

This website is simple!!!
Landing page background image should capture the customers attention!!! We will provide a image as a example of what we like. The purpose for this website is to provide customers with a clean easy way to request a quote for industrial casters and wheels by OEM’s as well as maintenance departments worldwide. Please see if you can follow our thought process below.
Customer comes to website, they are invited to Request a Quote by providing us with Manufacturer Name, Manufacturers Part # and quantity needed.
If this is not known the customer will complete will WP conversation format form answering about 10 questions
Or
Look up the part number in one of the 8 to 12 catalogs located in the Flippin Book format on our catalog page, or equal plug in .
When the client request a quote a account page will pop up request The following:
Clients first and last name
Email address
And optional questions
Company name and best contact number.
Once this is complete customer will hit SUBMIT.
The customers request will be in system. A email will be sent to Customer service notifying us the Quote Request has been made.
We will then build a quote for the customer with a good, better and best options. Customers Request a Quote submission may have more than one caster or wheel requested at a time, so website must allow this.
When the customer comes back into website there email address will come up as the account name and request a password be made for them. This will allow them to store quotes in their account for future needs. If quote is older than 30 day the system will trigger a button at the bottom of the quote for resubmit Request for updated quote.
Once customer reviews quote the quote can be Converted to order within the website.
Once Converted the system will send us a email and order will be processed.
We will need a Chat program that will text to CS the questions.
You will need to have high quality graphic design skills on your team.
We have found 2 plugins that would work nicely with our new website Flippin books to showcase our catalogs for customers to research and WPForms conversation forms to complete request for quote form.
Just Ideas:
Very very ghosted caster blueprint in white background but very very ghosted or the icon just idea
We have never had a font used we like
Grayscale every except for rubber on wheels and logo icon
Website should have hamburger menu on left
Website should hav responsive deign
Account head on right side
Has anyone read the brief from top to bottom and the updates, I’m seeing a lot of duplicates of the website I posted in images I want a clean website With lite backgrand with the poly being definite colors on each wheel I added a green yellow and red image has anyone looked at that Just a question?
Went on vacation/holiday

```html
<!DOCTYPE html>
<html lang="en">
<head>
<meta charset="utf-8">
<title>Pivots &amp; Treads .com — Request a Quote</title>
<link rel="stylesheet" href="https://fonts.googleapis.com/css2?family=Noto+Sans:wght@400;600;700;800&family=Nunito:wght@400;600&display=swap">
<style>
  :root {
    --brand: #27479a;
    --ink: #232633;
    --muted: #7d8293;
    --line: #e3e6ee;
    --step-bg: #e7ebf6;
    --star: #f2b531;
    --white: #ffffff;
  }
  * { box-sizing: border-box; margin: 0; padding: 0; }
  html, body { width: 1200px; height: 675px; overflow: hidden; }
  body { background: var(--brand); font-family: "Noto Sans", sans-serif; color: var(--ink); position: relative; }
  .page { position: absolute; left: 100px; top: 56px; width: 1000px; height: 563px; background: var(--white); border-radius: 16px; }
  .abs { position: absolute; }

  .brand { left: 84px; top: 34px; display: flex; align-items: center; gap: 8px; }
  .brand-dot { width: 18px; height: 18px; border-radius: 50%; background: var(--brand); }
  .brand-name { font-weight: 800; font-size: 13px; color: var(--ink); letter-spacing: 0.1px; }

  .account { right: 84px; top: 34px; display: flex; align-items: center; gap: 9px; }
  .account-text { text-align: right; line-height: 1.15; }
  .account-name { font-size: 7px; font-weight: 600; }
  .account-mail { font-size: 6.5px; color: var(--ink); }
  .avatar { width: 26px; height: 27px; border-radius: 5px; background: linear-gradient(160deg, #d9cfc4, #8f9aa6); }

  .headline { left: 84px; top: 89px; font-size: 37px; font-weight: 800; line-height: 44px; letter-spacing: -0.2px; }
  .headline .accent { color: var(--brand); }

  .review { left: 90px; top: 290px; border-left: 2px solid var(--brand); padding: 2px 0 2px 11px; font-family: "Nunito", sans-serif; }
  .stars { color: var(--star); font-size: 7px; letter-spacing: 2px; margin-bottom: 3px; }
  .review p { font-size: 8.6px; line-height: 14px; color: var(--ink); }

  .hero-photo { left: 418px; top: 158px; width: 176px; height: 198px; border-radius: 14px;
    background: radial-gradient(circle at 42% 64%, #3447a6 0%, #283a8c 40%, #c9ccd4 62%, #eceef2 100%); }

  .dots { left: 618px; top: 277px; display: flex; flex-direction: column; gap: 8px; }
  .dots span { width: 6px; height: 6px; border-radius: 50%; background: #c3c9da; }
  .dots span:first-child { background: var(--brand); }

  .steps { left: 738px; top: 265px; }
  .steps h3 { font-size: 9.5px; font-weight: 600; margin-bottom: 12px; }
  .step { display: flex; align-items: center; gap: 8px; height: 26px; margin-bottom: 10.5px; font-size: 9.5px; font-weight: 500; }
  .step-num { width: 26px; height: 26px; border-radius: 4px; background: var(--step-bg); color: var(--brand); display: flex; align-items: center; justify-content: center; font-size: 12px; font-weight: 600; }

  .cue { left: 70px; top: 392px; z-index: 2; overflow: visible; }

  .quote-bar { left: 84px; top: 452px; width: 832px; height: 71px; background: var(--white); border-radius: 6px; box-shadow: 0 4px 18px rgba(30, 45, 90, 0.08); display: flex; align-items: center; padding: 0 28px; gap: 10px; }
  .quote-title { font-size: 13px; font-weight: 600; width: 114px; }
  .field { height: 35px; border: 1px solid var(--line); border-radius: 4px; display: flex; align-items: center; gap: 9px; padding: 0 14px; font-family: "Nunito", sans-serif; font-size: 7.8px; color: var(--muted); }
  .field.wide { width: 215px; }
  .field.qty { width: 63px; justify-content: space-between; padding: 0 10px; color: var(--ink); }
  .field .hash { font-size: 11px; color: var(--muted); }
  .submit { width: 130px; height: 35px; border: 0; border-radius: 4px; background: var(--brand); color: var(--white); font-family: "Noto Sans", sans-serif; font-size: 8.5px; font-weight: 700; }
</style>
</head>
<body>
  <main class="page">
    <header>
      <div class="abs brand"><span class="brand-dot"></span><span class="brand-name">PIVOTS &amp; TREADS</span></div>
      <div class="abs account">
        <div class="account-text">
          <div class="account-name">Nora Hale</div>
          <div class="account-mail">norahale@example.com</div>
        </div>
        <div class="avatar" role="img" aria-label="Account profile photo"></div>
      </div>
    </header>

    <h1 class="abs headline"><span class="accent">#1 Solutions</span><br>for all your<br>applications</h1>

    <blockquote class="abs review">
      <div class="stars">★★★★★</div>
      <p>“ The best product in the market,<br>high quality and recommended”</p>
    </blockquote>

    <div class="abs hero-photo" role="img" aria-label="Photo of an industrial swivel caster with a blue polyurethane wheel"></div>

    <div class="abs dots"><span></span><span></span><span></span></div>

    <section class="abs steps">
      <h3>3 Easy Steps...</h3>
      <div class="step"><span class="step-num">1</span>Request a quote</div>
      <div class="step"><span class="step-num">2</span>Receive a quote</div>
      <div class="step"><span class="step-num">3</span>Convert a quote to order</div>
    </section>

    <form class="abs quote-bar">
      <span class="quote-title">Request a Quote</span>
      <label class="field wide">
        <svg width="9" height="10" viewBox="0 0 9 10" fill="none" stroke="#7d8293" stroke-width="0.9"><circle cx="4.5" cy="3" r="2.2"/><path d="M0.7 9.5 C1 6.8 8 6.8 8.3 9.5"/></svg>
        Enter Manufacturer Name
      </label>
      <label class="field wide"><span class="hash">#</span>Manufacturers Part #</label>
      <label class="field qty"><span>Qty</span><span style="color:#7d8293">0</span></label>
      <button type="button" class="submit">Request For Quotation</button>
    </form>

    <svg class="abs cue" width="60" height="80" viewBox="0 0 60 80" fill="none" stroke="#27479a" stroke-width="1.6" stroke-linecap="round" stroke-linejoin="round">
      <path d="M3 4 C30 4 57 16 54 30 C51 42 18 42 14 55 C12 64 30 70 48 69"/>
      <path d="M43 64 L48 69 L43 74"/>
    </svg>
  </main>
</body>
</html>
```